Become a real French Pastry chef with an easy 3 step pastry kit box.

The company is specialized in French pastries and the boxes will be sold online, and retail stores. The goal is for anyone who likes to be creative and crafty to create and bake their own traditional french pastry in 3 easy steps right at home. French pastries can be known to take hours to bake. These boxes allow you to make them very quickly, no hassle and they results taste amazing. All the ingredients are from FRANCE. Everything you need is in the box, All you need is water! The box design desired is elegant, simple, glamorous but yet eye catchy for retail distribution. This is a kit box with pre scaled ingredients to make your own eclairs. Box dimensions are 8x6x2.
Updates

Target Market(s)

Middle Aged, middle to upper class housewives who enjoy cooking and baking

Industry/Entity Type

Bakery

Font styles to use
Decorative
Script

Colors

Designer to choose colors to be used in the design.

Requirements
Must have
• This box will be called "The eclair kit by {logo}, or {logo} presents the Eclair kit.
• Has to have the instructions (attached document)
• "This box contains: 4 éclair shells, powder pouch, icing bag, pipping bag and pipping tip"
• Net weight 245g
• Nutrition label (attached)
Nice to have
• An eclair on it.

```html
<!DOCTYPE html>
<html lang="en">
<head>
<meta charset="utf-8">
<title>The Éclair Kit – Box Panels</title>
<link rel="stylesheet" href="https://fonts.googleapis.com/css2?family=Great+Vibes&family=Parisienne&family=Cormorant+Garamond:wght@500;600&display=swap">
<style>
  :root {
    --stage-top: #f4f6f7;
    --stage-bottom: #b9c3c8;
    --panel: #ffffff;
    --gold: #b8922e;
    --gold-light: #e3c766;
    --brown: #a4603f;
    --ink-blue: #3a6fb5;
    --splash-red: #ec8a8c;
    --splash-blue: #8d97cf;
    --splash-pink: #f6d9d6;
    --chocolate: #5b3a2c;
    --shadow: rgba(40, 55, 65, 0.18);
  }
  * { box-sizing: border-box; margin: 0; padding: 0; }
  html, body { width: 1200px; height: 923px; overflow: hidden; }
  body {
    background: linear-gradient(180deg, var(--stage-top), var(--stage-bottom));
    position: relative;
    font-family: "Cormorant Garamond", serif;
  }
  .panel {
    position: absolute;
    background: var(--panel);
    box-shadow: 0 6px 18px var(--shadow);
    overflow: hidden;
  }

  /* Lid top */
  .panel--top { left: 300px; top: 30px; width: 870px; height: 480px; }
  .brand {
    position: absolute; left: 40px; top: 48px;
    display: flex; align-items: center; gap: 10px;
    font-weight: 600; font-size: 24px; color: var(--ink-blue);
  }
  .brand__dot { width: 14px; height: 14px; border-radius: 50%; background: var(--ink-blue); }
  .presents {
    position: absolute; left: 250px; top: 58px;
    font-family: "Parisienne", cursive; font-size: 28px; color: var(--gold);
  }
  .steps-badge {
    position: absolute; right: 70px; top: 30px;
    font-family: "Great Vibes", cursive; color: var(--gold);
    font-size: 26px; line-height: 0.9; transform: rotate(-8deg);
  }
  .steps-badge b { font-size: 52px; font-weight: 400; vertical-align: middle; }
  .title {
    position: absolute; left: 260px; top: 95px;
    display: flex; align-items: baseline; gap: 10px;
    font-family: "Great Vibes", cursive; font-weight: 400; color: var(--gold);
    text-shadow: 0 2px 0 var(--gold-light), 0 3px 6px rgba(0,0,0,0.25);
    line-height: 1;
  }
  .title__the { font-size: 52px; }
  .title__name { font-size: 124px; }
  .title__kit { font-size: 92px; position: relative; top: 22px; }
  .hero-art {
    position: absolute; left: 120px; top: 255px; width: 540px; height: 200px;
    border-radius: 8px;
    background: linear-gradient(100deg, var(--splash-pink) 0%, var(--splash-red) 40%, var(--splash-blue) 80%, var(--splash-pink) 100%);
  }
  .net-weight {
    position: absolute; right: 40px; top: 260px;
    font-size: 22px; font-weight: 500; color: var(--chocolate);
    transform: rotate(-6deg);
  }

  /* Front */
  .panel--front { left: 300px; top: 530px; width: 870px; height: 360px; }
  .ornament {
    position: absolute; left: 20px; top: 20px; width: 120px; height: 320px;
    background: linear-gradient(160deg, #f5ebc6, #ead9a0);
    border-radius: 6px;
  }
  .slogan {
    position: absolute; left: 185px; top: 125px;
    font-family: "Great Vibes", cursive; font-size: 56px; line-height: 1.2;
    color: var(--brown); transform: rotate(-8deg); transform-origin: left center;
    white-space: nowrap;
  }
  .slogan__second { display: block; margin-left: 50px; }
  .chef-art {
    position: absolute; right: 30px; top: 20px; width: 150px; height: 320px;
    background: linear-gradient(180deg, #f7e8df, #e7c2ae);
    border-radius: 8px;
  }

  /* Side */
  .panel--side { left: 30px; top: 530px; width: 250px; height: 360px; padding: 24px 22px; }
  .includes__title {
    font-weight: 600; font-size: 30px; color: var(--brown);
    text-decoration: underline; margin-bottom: 14px;
  }
  .includes__list { list-style: none; display: flex; flex-direction: column; gap: 6px; }
  .includes__item {
    display: flex; align-items: center; gap: 12px;
    font-size: 18px; line-height: 1.15; color: var(--brown);
  }
  .includes__item svg { flex: none; }
  .plus { color: var(--brown); font-size: 20px; margin-left: 12px; line-height: 0.8; }
</style>
</head>
<body>

<section class="panel panel--top">
  <div class="brand"><span class="brand__dot"></span>Maison Clairette</div>
  <div class="presents">presents</div>
  <div class="steps-badge"><b>3</b> easy<br>&nbsp;&nbsp;&nbsp;&nbsp;steps</div>
  <div class="hero-art" role="img" aria-label="Watercolour painting of a chocolate-glazed éclair over red and blue paint splashes"></div>
  <h1 class="title">
    <span class="title__the">the</span><span class="title__name">Éclair</span><span class="title__kit">kit</span>
  </h1>
  <div class="net-weight">Net wt. 245g</div>
</section>

<section class="panel panel--front">
  <div class="ornament" role="img" aria-label="Gold flourish ornament"></div>
  <p class="slogan">Become a pastry chef<span class="slogan__second">in 3 easy steps!</span></p>
  <div class="chef-art" role="img" aria-label="Line drawing of a pastry chef holding an éclair"></div>
</section>

<aside class="panel panel--side">
  <h2 class="includes__title">Includes:</h2>
  <ul class="includes__list">
    <li class="includes__item">
      <svg width="34" height="20" viewBox="0 0 34 20"><rect x="2" y="5" width="30" height="10" rx="5" fill="none" stroke="var(--brown)" stroke-width="1.6"/></svg>
      4 éclair shells
    </li>
    <li class="plus">+</li>
    <li class="includes__item">
      <svg width="34" height="28" viewBox="0 0 34 28"><rect x="7" y="2" width="20" height="24" rx="2" fill="none" stroke="var(--brown)" stroke-width="1.6"/></svg>
      powder pouch
    </li>
    <li class="plus">+</li>
    <li class="includes__item">
      <svg width="34" height="28" viewBox="0 0 34 28"><path d="M9 3h16l-3 22H12z" fill="none" stroke="var(--brown)" stroke-width="1.6"/></svg>
      icing bag
    </li>
    <li class="plus">+</li>
    <li class="includes__item">
      <svg width="34" height="30" viewBox="0 0 34 30"><path d="M6 3h22L18 25h-2z" fill="none" stroke="var(--brown)" stroke-width="1.6"/><path d="M15 25h4v3h-4z" fill="var(--brown)"/></svg>
      <span>piping bag &amp;<br>piping tip</span>
    </li>
  </ul>
</aside>

</body>
</html>
```